Bright Harbor Motors Business Card

Would like a cutting edge / high end Automotive Business card design. Please see current card which is old and dated. Would like to maintain the Bright Harbor Motors logo and same information (address, website, etc).

See our website for the look and feel of what we offer - www.brightharbormotors.example

Target Market(s)

Upper class car buyers

Contact Information for Business Card

Modern high end business card design

Requirements
Nice to have
• Carbon Fiber look background

```html
<!DOCTYPE html>
<html lang="en">
<head>
<meta charset="utf-8">
<title>Bright Harbor Motors – Business Card</title>
<link rel="stylesheet" href="https://fonts.googleapis.com/css2?family=Montserrat:wght@300;400;700&family=Libre+Baskerville&display=swap">
<style>
  :root {
    --card-black: #141314;
    --texture-dark: #1c1b1c;
    --texture-light: #2a2829;
    --text-white: #ffffff;
    --band-top: #050505;
    --band-bottom: #4a0b0f;
    --band-edge: #7a1015;
    --gold: #e2c77c;
    --brand-cream: #efe3bf;
    --car-red: #d8141c;
    --car-dark: #7d0a0e;
  }
  html, body {
    margin: 0;
    padding: 0;
    width: 1200px;
    height: 686px;
    overflow: hidden;
    background: var(--card-black);
  }
  .card {
    position: relative;
    width: 1200px;
    height: 686px;
    overflow: hidden;
    font-family: "Montserrat", sans-serif;
    color: var(--text-white);
  }
  .card-texture {
    position: absolute;
    inset: 0;
    background: radial-gradient(ellipse at 45% 40%, var(--texture-light) 0%, var(--texture-dark) 55%, var(--card-black) 100%);
  }
  .identity {
    position: absolute;
    left: 122px;
    top: 112px;
  }
  .person-name {
    margin: 0;
    font-size: 55px;
    font-weight: 700;
    line-height: 1.1;
  }
  .person-title {
    margin: 12px 0 0;
    font-size: 36px;
    font-weight: 300;
    letter-spacing: 5px;
    line-height: 1.1;
  }
  .contact-list {
    position: absolute;
    left: 122px;
    top: 328px;
    margin: 0;
    font-size: 25px;
    font-weight: 400;
  }
  .contact-row {
    display: flex;
    height: 34px;
    align-items: center;
    margin-bottom: 33px;
  }
  .contact-label { width: 161px; margin: 0; }
  .contact-sep { width: 117px; }
  .contact-value { margin: 0; }
  .footer-band {
    position: absolute;
    left: 0;
    top: 566px;
    width: 1200px;
    height: 120px;
    background: linear-gradient(to bottom, var(--band-top) 0%, var(--band-top) 30%, var(--band-bottom) 100%);
    border-left: 4px solid var(--band-edge);
    border-right: 4px solid var(--band-edge);
    box-sizing: border-box;
  }
  .brand-name {
    position: absolute;
    left: 22px;
    top: 24px;
    width: 260px;
    font-family: "Montserrat", sans-serif;
    font-size: 27px;
    font-weight: 400;
    line-height: 1.25;
    color: var(--brand-cream);
    text-align: center;
  }
  .tagline {
    position: absolute;
    left: 392px;
    top: 30px;
    width: 400px;
    margin: 0;
    font-family: "Libre Baskerville", serif;
    font-size: 20px;
    line-height: 30px;
    color: var(--gold);
    text-align: center;
  }
  .car-visual {
    position: absolute;
    left: 926px;
    top: 12px;
    width: 260px;
    height: 100px;
    border-radius: 60px 90px 20px 20px;
    background: radial-gradient(ellipse at 55% 35%, var(--car-red) 0%, var(--car-dark) 100%);
  }
</style>
</head>
<body>
  <main class="card">
    <div class="card-texture" role="img" aria-label="Dark hexagonal carbon-style background texture"></div>

    <header class="identity">
      <h1 class="person-name">Dana Merrow</h1>
      <p class="person-title">OWNER</p>
    </header>

    <dl class="contact-list">
      <div class="contact-row">
        <dt class="contact-label">Phone</dt><span class="contact-sep">:</span><dd class="contact-value">415.555.0148</dd>
      </div>
      <div class="contact-row">
        <dt class="contact-label">Fax</dt><span class="contact-sep">:</span><dd class="contact-value">415.555.0192</dd>
      </div>
      <div class="contact-row">
        <dt class="contact-label">Email</dt><span class="contact-sep">:</span><dd class="contact-value">dana@brightharbormotors.example</dd>
      </div>
    </dl>

    <footer class="footer-band">
      <div class="brand-name">Bright Harbor Motors</div>
      <p class="tagline">Offering the Finest in<br>Exotic/Luxury Sports Cars</p>
      <div class="car-visual" role="img" aria-label="Red exotic sports car"></div>
    </footer>
  </main>
</body>
</html>
```